Website Nudges/Banners for 5* hotels

Dear PixelGuild Community,
We are a small hotel chain in the Indian Ocean and we are looking for a
nudge/banner design for our website to push our offers and/or Unique selling point to our visitors.
We would like to see some fresh designs to be used on the website in JPEG or PNG.
We will need the PSD version as well to amend and correct the wording when needed.
We have attached a few files to help you to understand more what we are looking for:
- An example of an existing nudge/banner that we are using on our website (336x200)
- A Screenshot of our nudge appearing on our website page to help you visualize how it will look live.
- Our Brand Guideline
- Some symbols that we use on our website (https://www.marivelstays.com/en/) and other materials to highlight text.
Should you need images, you can use an image you like at https://www.marivelstays.com/en/gallery/.
I hope that you will find this small project interesting and challenging.
Thank you!

Worldwide

Hospitality

• Gill Sans Nova

• The banners need to be elegant and catchy

```html
<!DOCTYPE html>
<html lang="en">
<head>
<meta charset="utf-8">
<title>Holiday in Maldives – Marivel Lunavaru offer banner</title>
<link rel="stylesheet" href="https://fonts.googleapis.com/css2?family=Great+Vibes&family=Montserrat:wght@400;700&display=swap">
<style>
  :root {
    --ink: #1c3340;
    --teal: #3dbdb5;
    --white: #ffffff;
    --photo-light: #8fc3dd;
    --photo-mid: #3f9fcf;
    --photo-deep: #1f6aa8;
  }
  * { margin: 0; padding: 0; box-sizing: border-box; }
  html, body { width: 1200px; height: 763px; overflow: hidden; background: var(--white); }
  .banner {
    position: relative;
    width: 1200px;
    height: 763px;
    overflow: hidden;
    background: var(--white);
    font-family: "Montserrat", sans-serif;
  }
  .hero-photo {
    position: absolute;
    left: 0;
    top: 0;
    width: 1200px;
    height: 640px;
    background: linear-gradient(180deg, var(--photo-light) 0%, var(--photo-mid) 45%, var(--photo-deep) 100%);
  }
  .brush-edge {
    position: absolute;
    left: 0;
    top: 470px;
    width: 1200px;
    height: 180px;
  }
  .title-ring {
    position: absolute;
    left: 340px;
    top: 18px;
    width: 470px;
    height: 470px;
    border: 2px solid rgba(255,255,255,0.92);
    border-radius: 50%;
  }
  .title {
    position: absolute;
    left: 325px;
    top: 150px;
    width: 500px;
    text-align: center;
    font-family: "Great Vibes", cursive;
    font-weight: 400;
    color: var(--white);
    font-size: 98px;
    line-height: 104px;
  }
  .title-line-2 { display: block; padding-left: 40px; }
  .offer-headline,
  .offer-venue {
    position: absolute;
    left: 80px;
    text-transform: uppercase;
    white-space: nowrap;
  }
  .offer-headline {
    top: 660px;
    font-weight: 700;
    font-size: 50px;
    line-height: 50px;
    letter-spacing: 1px;
    color: var(--ink);
  }
  .offer-venue {
    top: 723px;
    font-weight: 400;
    font-size: 42px;
    line-height: 42px;
    letter-spacing: 0.5px;
    color: var(--teal);
  }
  .cta {
    position: absolute;
    left: 852px;
    top: 686px;
    width: 294px;
    height: 77px;
    display: flex;
    align-items: center;
    justify-content: center;
    background: var(--teal);
    color: var(--white);
    border-radius: 38px 22px 0 12px;
    font-weight: 700;
    font-size: 30px;
    letter-spacing: 1px;
    text-decoration: none;
    text-transform: uppercase;
  }
</style>
</head>
<body>
  <main class="banner">
    <div class="hero-photo" role="img" aria-label="Aerial photo of a Maldives island resort with overwater villas in a turquoise lagoon"></div>

    <svg class="brush-edge" viewBox="0 0 1200 180" preserveAspectRatio="none" aria-hidden="true">
      <path fill="#ffffff" d="M0 40 L30 30 L55 12 L80 40 L110 28 L135 58 L170 66 L210 84 L250 92 L300 100 L360 104 L420 110 L480 114 L530 120 L580 124 L640 118 L700 110 L760 104 L800 90 L840 84 L880 70 L915 62 L950 48 L985 56 L1020 34 L1055 44 L1090 22 L1125 36 L1160 18 L1200 30 L1200 180 L0 180 Z"/>
    </svg>

    <div class="title-ring" aria-hidden="true"></div>
    <h1 class="title">Holiday in<span class="title-line-2">Maldives</span></h1>

    <p class="offer-headline">Enjoy 40% discount</p>
    <p class="offer-venue">at Marivel Lunavaru</p>

    <a class="cta" href="#">Discover</a>
  </main>
</body>
</html>
```